Billboard For Marek Delvaine

Need a Billboard 8ft. High x 16ft. Long. Ive attached a former billboard and looking for the same thing just updated with:
Summit Lodge Award Logo - 2020, 2022
Pinnacle Ring award Logo - 2022

Thanks.

```html
<!DOCTYPE html>
<html lang="en">
<head>
<meta charset="utf-8">
<title>Billboard – Marek Delvaine</title>
<link rel="stylesheet" href="https://fonts.googleapis.com/css2?family=Montserrat:ital,wght@1,800&family=Oswald:wght@300;400&family=Poppins:ital,wght@0,400;0,500;0,600;1,500&display=swap">
<style>
  :root {
    --ink: #0d0d0d;
    --red: #e31b2b;
    --paper: #ffffff;
    --grey: #333333;
    --shirt: #3d4f9e;
    --skin: #e8c9b8;
    --rule: #bbbbbb;
  }
  * { margin: 0; padding: 0; box-sizing: border-box; }
  html, body { width: 1200px; height: 600px; overflow: hidden; background: var(--paper); }
  .billboard { position: relative; width: 1200px; height: 600px; background: var(--paper); overflow: hidden; font-family: "Poppins", sans-serif; color: var(--ink); }

  .portrait {
    position: absolute; left: 0; top: 0; width: 500px; height: 600px;
    background: linear-gradient(180deg, #f4f4f4 0%, var(--skin) 30%, #d9ad98 55%, var(--shirt) 72%, #2f3f86 100%);
  }

  .headline {
    position: absolute; font-family: "Montserrat", sans-serif; font-weight: 800; font-style: italic;
    font-size: 72px; line-height: 1; letter-spacing: -2px; white-space: nowrap;
  }
  .headline--one { left: 480px; top: 52px; }
  .headline--two { left: 556px; top: 124px; }
  .headline .accent { color: var(--red); }

  .contact-frame { position: absolute; left: 0; top: 0; width: 1200px; height: 600px; pointer-events: none; }

  .agent-name {
    position: absolute; left: 556px; width: 506px; top: 232px; text-align: center;
    font-weight: 600; font-size: 54px; line-height: 1; letter-spacing: 0.5px; white-space: nowrap;
  }
  .agent-title {
    position: absolute; left: 474px; width: 652px; top: 289px; text-align: center;
    font-weight: 400; font-size: 20px; letter-spacing: 6px; color: var(--grey);
  }
  .agent-phone {
    position: absolute; left: 474px; width: 652px; top: 308px; text-align: center;
    font-weight: 600; font-size: 96px; line-height: 1.05; letter-spacing: -1px; color: var(--red);
  }
  .tagline {
    position: absolute; left: 474px; width: 652px; top: 420px; text-align: center;
    font-weight: 400; font-size: 31px; line-height: 1.2; letter-spacing: 0.8px; white-space: nowrap;
  }
  .tagline em { color: var(--red); font-style: italic; font-weight: 500; }

  .award { position: absolute; display: flex; align-items: center; gap: 10px; }
  .award-seal { flex: none; border: 2px solid var(--ink); border-radius: 50%; background: var(--paper); }
  .award--summit { left: 496px; top: 490px; }
  .award--summit .award-seal { width: 62px; height: 62px; }
  .award--pinnacle { left: 715px; top: 500px; }
  .award--pinnacle .award-seal { width: 42px; height: 42px; background: var(--ink); }
  .award-text { font-family: "Oswald", sans-serif; line-height: 1; color: var(--ink); white-space: nowrap; }
  .award-brand { font-family: "Poppins", sans-serif; font-size: 9px; letter-spacing: 0.3px; margin-bottom: 2px; }
  .award-name { font-weight: 400; font-size: 21px; letter-spacing: -0.3px; }
  .award-line { display: flex; align-items: center; }
  .award-rank { font-family: "Poppins", sans-serif; font-size: 6.5px; line-height: 1.15; border-left: 1px solid var(--ink); padding-left: 3px; margin-left: 6px; }
  .award-year { font-weight: 300; font-size: 16px; margin-top: 1px; }
  .award--pinnacle .award-name { font-weight: 300; font-size: 21px; }

  .brokerage { position: absolute; left: 914px; top: 500px; width: 146px; text-align: center; }
  .brokerage-name { font-weight: 600; font-size: 17px; line-height: 1.2; color: var(--ink); }
  .brokerage-office { font-weight: 400; font-size: 10px; margin-top: 12px; }
  .brokerage-note { font-weight: 400; font-size: 6px; margin-top: 1px; }

  .social { position: absolute; left: 1072px; top: 518px; display: flex; align-items: center; gap: 5px; font-weight: 500; font-size: 10px; color: var(--red); }
  .social-divider { width: 1px; height: 26px; background: var(--rule); }
</style>
</head>
<body>
<main class="billboard">
  <div class="portrait" role="img" aria-label="Portrait photo of Marek Delvaine smiling, wearing a blue shirt and patterned tie"></div>

  <h1 class="headline headline--one">BUYING OR</h1>
  <p class="headline headline--two">SELLING? <span class="accent">CALL</span></p>

  <svg class="contact-frame" viewBox="0 0 1200 600" aria-hidden="true">
    <path d="M554 266 H497 A24 24 0 0 0 473 290 V389 A24 24 0 0 0 497 413 H1100 A24 24 0 0 0 1124 389 V290 A24 24 0 0 0 1100 266 H1062" fill="none" stroke="#e31b2b" stroke-width="3"/>
  </svg>

  <h2 class="agent-name">MAREK DELVAINE</h2>
  <p class="agent-title">SALES REPRESENTATIVE</p>
  <p class="agent-phone">613.555.0148</p>
  <p class="tagline">FOCUSED, DRIVEN, AND <em>EXPERIENCED!</em></p>

  <div class="award award--summit">
    <div class="award-seal"></div>
    <div class="award-text">
      <div class="award-brand">CROWN HEARTH</div>
      <div class="award-name">SUMMIT</div>
      <div class="award-line"><span class="award-name">LODGE</span><span class="award-rank">NATIONAL<br>TOP 1%</span></div>
      <div class="award-year">AWARD 2020, 2022</div>
    </div>
  </div>

  <div class="award award--pinnacle">
    <div class="award-seal"></div>
    <div class="award-text">
      <div class="award-brand">CROWN HEARTH</div>
      <div class="award-name">PINNACLE RING</div>
      <div class="award-name">AWARD 2022</div>
    </div>
  </div>

  <div class="brokerage">
    <div class="brokerage-name">CROWN HEARTH</div>
    <div class="brokerage-office">ASHFORD &amp; ASSOCIATES</div>
    <div class="brokerage-note">INDEPENDENTLY OWNED AND OPERATED</div>
  </div>

  <div class="social">
    <span>Friendsy</span>
    <span class="social-divider"></span>
    <span>Pixgram</span>
  </div>
</main>
</body>
</html>
```